Young, modern, highly skilled carpenter needs business card design

I need a business card design for my construction business. Its called 'Pemberton Building Partners'. Im looking for a ultra modern design that incorporates P B P, the first letters of the name with only a subtle reference to carpentry. The design should reflect my high quality work and eye for detail. i have also uploaded some exmaple designs i like.

Industry/Entity Type

Construction

Requirements
Must have
• Name of business, my name, mobile number, ABN number, email address
Nice to have
• A logo incorporating the name of the business

```html
<!DOCTYPE html>
<html lang="en">
<head>
<meta charset="utf-8">
<title>Pemberton Building Partners – Business Card</title>
<link rel="stylesheet" href="https://fonts.googleapis.com/css2?family=EB+Garamond:wght@600;700&family=Mulish:wght@700&family=Noto+Sans:wght@400&display=swap">
<style>
  :root {
    --paper: #ffffff;
    --ink: #111111;
    --muted: #777777;
    --accent: #b8834a;
    --rule: #888888;
    --shadow: #9a9a9a;
    --wood-light: #b5773a;
    --wood-mid: #9a5f28;
    --wood-dark: #7d4a1e;
  }
  * { margin: 0; padding: 0; box-sizing: border-box; }
  html, body { width: 1200px; height: 605px; overflow: hidden; background: var(--paper); }
  .canvas { position: relative; width: 1200px; height: 605px; }

  .wood {
    position: absolute;
    background: linear-gradient(180deg, var(--wood-mid) 0%, var(--wood-light) 35%, var(--wood-mid) 60%, var(--wood-light) 80%, var(--wood-dark) 100%);
    box-shadow: 3px 3px 0 var(--shadow);
  }

  /* Front card */
  .card-front { position: absolute; left: 35px; top: 41px; width: 555px; height: 333px; }
  .card-front .wood { left: 0; top: 0; width: 555px; height: 157px; }
  .card-front .frame {
    position: absolute; left: 0; top: 157px; width: 555px; height: 176px;
    border-left: 1px solid var(--ink); border-right: 1px solid var(--rule); border-bottom: 1px solid var(--rule);
  }
  .business-name {
    position: absolute; left: 0; width: 555px; top: 96px; text-align: center;
    font-family: "Mulish", sans-serif; font-weight: 700; font-size: 27px; letter-spacing: 0.3px;
    color: var(--paper); text-shadow: 2px 2px 2px #2a1a0c;
  }
  .name-rule {
    position: absolute; left: 53px; top: 136px; width: 455px; height: 3px;
    background: var(--paper); box-shadow: 2px 2px 2px #2a1a0c;
  }
  .services {
    position: absolute; left: 0; width: 555px; top: 168px; text-align: center;
    font-family: "EB Garamond", serif; font-weight: 700; font-size: 25px; color: var(--ink);
  }
  .services .dot { color: var(--accent); margin: 0 10px; }
  .services-note {
    position: absolute; left: 0; width: 545px; top: 206px; text-align: center;
    font-family: "EB Garamond", serif; font-weight: 600; font-size: 20px; color: var(--muted);
  }

  /* Back card */
  .card-back .wood { left: 609px; top: 215px; width: 213px; height: 335px; }
  .logo-name {
    position: absolute; left: 609px; top: 350px; width: 213px; text-align: center;
    font-family: "Noto Sans", sans-serif; font-weight: 400; font-size: 44px; letter-spacing: 6px; color: var(--ink);
  }
  .top-rule { position: absolute; left: 822px; top: 218px; width: 344px; height: 1px; background: var(--ink); }
  .person {
    position: absolute; left: 878px; top: 312px;
    font-family: "Noto Sans", sans-serif; font-size: 20px; letter-spacing: 0.8px; color: var(--ink);
  }
  .contact { position: absolute; left: 820px; top: 352px; font-family: "Noto Sans", sans-serif; }
  .contact .row { display: flex; height: 32px; align-items: center; }
  .contact dt { width: 97px; text-align: right; color: var(--accent); font-size: 15px; letter-spacing: 1px; }
  .contact dd { margin-left: 14px; color: var(--ink); font-size: 16px; letter-spacing: 0.8px; }
</style>
</head>
<body>
<main class="canvas">
  <section class="card-front">
    <div class="wood" role="img" aria-label="Warm oak wood grain texture"></div>
    <div class="frame"></div>
    <h1 class="business-name">Pemberton Building Partners</h1>
    <div class="name-rule"></div>
    <p class="services">Decking<span class="dot">•</span>Housing<span class="dot">•</span>Pergolas</p>
    <p class="services-note">&amp; all other aspects of carpentry</p>
  </section>

  <section class="card-back">
    <div class="wood" role="img" aria-label="Warm oak wood grain texture"></div>
    <div class="logo-name">PBP</div>
    <div class="top-rule"></div>
    <p class="person">Callum Ashdown</p>
    <dl class="contact">
      <div class="row"><dt>m. no.</dt><dd>9930418562</dd></div>
      <div class="row"><dt>email id.</dt><dd>callum@pembertonbp.com</dd></div>
      <div class="row"><dt>ABN no.</dt><dd>518204736915</dd></div>
    </dl>
  </section>
</main>
</body>
</html>
```